Corvella Paintless Dent Removal

Our company works on vehicles removing dents using a highly skilled trade which the metal is massaged out with special tools without disturbing the original paint, hence paintless dent removal. Besides keeping the paint and metal original its also very environmentally friendly since no paint or toxic fillers are used. Also we we are one of the most experienced companies in the business with 25 years

Target Market(s)

Retail Automobile consumers, Auto Dealerships and Auto Body Shops

Industry/Entity Type

Auto Repair

Contact Information for Business Card

Dennis Holbrook
PO Box 538 Ashmere, NY 11952
631-472-8816
corvellapdr@mailnest.example
website corvellapdr.example
youtube corvella paintless dent removal
25 years of experience removing Dents, Dings and Hail Damage

Font styles to use
Serif
Sans Serif

Colors

Designer to choose colors to be used in the design.

Requirements
Must have
• I do like things that are simple but classy and somewhat bold, also I like my logo so that should be somewhat important

```html
<!DOCTYPE html>
<html lang="en">
<head>
<meta charset="utf-8">
<title>Corvella Paintless Dent Removal – Business Card</title>
<link rel="stylesheet" href="https://fonts.googleapis.com/css2?family=Arimo:wght@700&family=Lato:wght@400&family=Crimson+Text:wght@600&display=swap">
<style>
  :root {
    --navy: #0c1a5e;
    --lime: #7cf500;
    --lime-shade: #6fae3a;
    --white: #ffffff;
  }
  html, body {
    margin: 0;
    padding: 0;
    overflow: hidden;
    background: var(--navy);
  }
  .card {
    position: relative;
    width: 1200px;
    height: 686px;
    background: var(--navy);
    overflow: hidden;
    font-family: "Lato", "Helvetica Neue", Arial, sans-serif;
    color: var(--white);
  }
  .badge {
    position: absolute;
    left: 0;
    top: 0;
    width: 1200px;
    height: 300px;
  }
  .brand {
    position: absolute;
    left: 300px;
    top: 52px;
    width: 600px;
    text-align: center;
    font-family: "Arimo", Arial, sans-serif;
    font-weight: 700;
    color: var(--navy);
    line-height: 1;
  }
  .brand-name {
    display: block;
    font-size: 66px;
    letter-spacing: -1px;
  }
  .brand-tagline {
    display: block;
    margin-top: 6px;
    font-size: 26px;
  }
  .vehicle-art {
    position: absolute;
    left: 771px;
    top: 206px;
    width: 429px;
    height: 405px;
    background: radial-gradient(ellipse at 70% 55%, rgba(124, 245, 0, 0.35), rgba(124, 245, 0, 0.08) 65%, rgba(124, 245, 0, 0) 80%);
  }
  .holder-name {
    position: absolute;
    left: 21px;
    top: 268px;
    margin: 0;
    font-family: "Arimo", Arial, sans-serif;
    font-weight: 700;
    font-size: 78px;
    letter-spacing: -0.5px;
    line-height: 1;
  }
  .address {
    position: absolute;
    left: 30px;
    top: 369px;
    margin: 0;
    font-size: 25px;
    line-height: 37px;
    font-style: normal;
  }
  .links {
    position: absolute;
    left: 30px;
    top: 462px;
    margin: 0;
    padding: 0;
    list-style: none;
  }
  .links li {
    display: flex;
    align-items: center;
    height: 46px;
    font-size: 25px;
  }
  .links svg,
  .links .video-mark {
    width: 36px;
    height: 30px;
    margin-right: 12px;
    flex: none;
  }
  .links .video-mark {
    width: 34px;
    height: 26px;
    margin-right: 14px;
    background: var(--white);
    border-radius: 6px;
  }
  .experience-band {
    position: absolute;
    left: 0;
    top: 606px;
    width: 1200px;
    height: 64px;
  }
  .experience-text {
    position: absolute;
    left: 190px;
    top: 606px;
    width: 820px;
    height: 64px;
    display: flex;
    align-items: center;
    justify-content: center;
    font-family: "Crimson Text", Georgia, serif;
    font-weight: 600;
    font-size: 29px;
    color: var(--navy);
  }
</style>
</head>
<body>
<div class="card">
  <svg class="badge" viewBox="0 0 1200 300" aria-hidden="true">
    <ellipse cx="614" cy="110" rx="372" ry="160" fill="var(--lime-shade)"/>
    <ellipse cx="600" cy="97" rx="375" ry="160" fill="var(--white)"/>
  </svg>
  <div class="brand">
    <span class="brand-name">Corvella</span>
    <span class="brand-tagline">Paintless Dent Removal</span>
  </div>

  <div class="vehicle-art" role="img" aria-label="Line illustration of the front of a sports car in lime green"></div>

  <h1 class="holder-name">Dennis Holbrook</h1>
  <address class="address">
    PO Box 538 Ashmere, NY 11952<br>
    631-472-8816
  </address>

  <ul class="links">
    <li>
      <svg viewBox="0 0 36 30" aria-hidden="true">
        <rect x="2" y="5" width="32" height="21" fill="none" stroke="var(--white)" stroke-width="2.5"/>
        <polyline points="2,5 18,18 34,5" fill="none" stroke="var(--white)" stroke-width="2.5"/>
        <line x1="2" y1="26" x2="14" y2="14" stroke="var(--white)" stroke-width="2"/>
        <line x1="34" y1="26" x2="22" y2="14" stroke="var(--white)" stroke-width="2"/>
      </svg>
      corvellapdr@mailnest.example
    </li>
    <li>
      <svg viewBox="0 0 36 30" aria-hidden="true">
        <circle cx="18" cy="15" r="13" fill="none" stroke="var(--white)" stroke-width="2.5"/>
        <ellipse cx="18" cy="15" rx="6" ry="13" fill="none" stroke="var(--white)" stroke-width="2"/>
        <line x1="5" y1="15" x2="31" y2="15" stroke="var(--white)" stroke-width="2"/>
        <line x1="7" y1="8" x2="29" y2="8" stroke="var(--white)" stroke-width="2"/>
        <line x1="7" y1="22" x2="29" y2="22" stroke="var(--white)" stroke-width="2"/>
      </svg>
      corvellapdr.example
    </li>
    <li>
      <span class="video-mark" aria-hidden="true"></span>
      corvella paintless dent removal
    </li>
  </ul>

  <svg class="experience-band" viewBox="0 0 1200 64" aria-hidden="true">
    <polygon points="104,0 128,0 104,32 128,64 104,64 80,32" fill="var(--lime)"/>
    <polygon points="148,0 172,0 148,32 172,64 148,64 124,32" fill="var(--lime)"/>
    <polygon points="208,0 1000,0 1024,32 1000,64 208,64 184,32" fill="var(--lime)"/>
    <polygon points="1020,0 1044,0 1068,32 1044,64 1020,64 1044,32" fill="var(--lime)"/>
    <polygon points="1064,0 1088,0 1112,32 1088,64 1064,64 1088,32" fill="var(--lime)"/>
  </svg>
  <div class="experience-text">25 years of experience removing Dents, Dings and Hail Damage</div>
</div>
</body>
</html>
```